Create a landing page for a new product market combination for an international software company

We are a software company being in the BtoB market for over 20 years. Our product is a software tool that allows for very flexible and versatile cost calculations for companies. We sell to all industries in over 40 countries with 500 clients. We have fairly recently seen a succesfull "competitor" (www.veltrani.com) come up in the niche market of IT costing. This competitor has launched an independent platform with regards to managing IT costs (www.QRSguild.org). In this independent platform standards are set, events are organised and books are written. Since our software can handle all type of costing questions we can en already do play a role in IT costing. We have therefore become a sponsor of the QRS guild. Besides that we came accross the opportunity to buy the URL: www.qrssoftware.com Which we did. We are now looking for a design on that landing page that communicates the fact that the visitor has landed with a company that have in depth knowledge on the QRS subject and provide an effective an affordable tooling for QRS. Currently the difference between the professionalism of our own website (www.pricelumen.com) and that of the competitor (www.veltrani.com) and the independent council (www.qrsguild.org). is too big.

Target Market(s)

BtB with large IT spend

Number of Pages Required

1 page

Colors

Designer to choose colors to be used in the design.

Requirements
Must have
• A proffessional look and feel
Should not have
• Definetely not too much information and wording

```html
<!DOCTYPE html>
<html lang="en">
<head>
<meta charset="utf-8">
<title>QRS Software – Technology Business Management</title>
<link rel="stylesheet" href="https://fonts.googleapis.com/css2?family=Poppins:wght@300;400;500;600;700&display=swap">
<style>
:root{
  --orange:#f26522;
  --orange-dark:#d9531a;
  --navy:#12304f;
  --navy-deep:#0c2138;
  --blue:#1c5a92;
  --sky:#1ba6e5;
  --ink:#222;
  --muted:#555;
  --light:#f2f2f2;
  --footer:#4a4d50;
  --footer-dark:#3a3c3e;
  --white:#fff;
}
*{box-sizing:border-box;margin:0;padding:0}
html,body{width:1200px;height:2521px;overflow:hidden}
body{font-family:"Poppins",sans-serif;color:var(--ink);background:var(--white);position:relative}
.wrap{width:740px;margin:0 auto;position:relative}

/* top bar */
.topbar{height:24px;background:var(--navy-deep);color:#dfe6ee;font-size:8px}
.topbar .wrap{display:flex;justify-content:space-between;align-items:center;height:24px}
.flags{display:flex;gap:6px}
.flag{width:17px;height:11px;display:flex;flex-direction:column}
.flag span{flex:1}

/* nav */
.nav{height:52px;background:var(--white);box-shadow:0 1px 3px rgba(0,0,0,.1);position:relative;z-index:2}
.nav .wrap{display:flex;justify-content:space-between;align-items:center;height:52px}
.brand{display:flex;align-items:center;gap:7px;font-size:17px;font-weight:600;color:var(--orange)}
.brand i{width:18px;height:18px;background:var(--orange);display:block}
.menu{display:flex;align-items:center;gap:20px;font-size:10.5px;font-weight:600;color:var(--ink)}
.btn{display:inline-block;background:var(--orange);color:var(--white);font-size:9px;font-weight:600;padding:6px 14px;border-radius:2px;text-transform:uppercase}
.btn-ghost{background:#f4f4f4;color:#333;border:1px solid #ccc;text-transform:none}

/* hero */
.hero{height:324px;position:relative;background:linear-gradient(90deg,#8a5a3a 0%,#3b4d63 45%,#1d3e63 100%);overflow:hidden}
.hero-photo{position:absolute;right:250px;top:0;width:340px;height:324px;background:radial-gradient(ellipse at 60% 75%,#2f6fc4 0%,#2e5f9e 45%,transparent 70%)}
.hero-text{position:absolute;left:230px;top:78px;color:var(--white)}
.hero-text h1{font-size:36px;line-height:42px;font-weight:700}
.hero-text p{font-size:18px;font-weight:300;margin-top:6px}
.hero-text .btn{margin-top:32px;padding:9px 17px}

/* enable */
.enable{height:360px;background:linear-gradient(180deg,#1a3a5e,#16324f);position:relative}
.section-title{text-align:center;font-size:20px;font-weight:400;padding-top:36px}
.enable .section-title{color:var(--white)}
.cards{display:flex;gap:20px;margin-top:26px}
.card{width:170px;height:233px;background:var(--white);border-radius:3px;text-align:center;padding:22px 16px 0}
.card svg{width:60px;height:60px}
.card h3{font-size:13px;font-weight:400;line-height:17px;margin-top:14px;color:var(--ink)}
.card p{font-size:9.5px;line-height:16px;color:var(--muted);margin-top:12px}

/* foster */
.foster{height:329px;background:linear-gradient(180deg,#d8d8d8,#fafafa 40%,#d9d9d9)}
.foster .section-title{padding-top:36px}
.pillars{display:flex;justify-content:space-between;margin-top:24px}
.pillar{width:370px;text-align:center}
.pillar svg{width:80px;height:76px}
.pillar h3{font-size:13px;font-weight:500;margin-top:10px}
.pillar p{font-size:9.5px;line-height:16px;color:var(--muted);margin-top:10px;padding:0 12px}
.pillar .btn{margin-top:12px}

/* fiscal */
.fiscal{height:387px;position:relative;background:linear-gradient(100deg,#1e4f82 0%,#19406b 55%,#24476b 85%,#a25a2c 100%);color:var(--white)}
.fiscal .section-title{color:var(--white);padding-top:37px}
.disciplines{display:flex;justify-content:space-between;margin-top:24px;padding:0 10px}
.discipline{width:180px;text-align:center}
.discipline svg{width:66px;height:66px}
.discipline h3{font-size:13px;font-weight:500;line-height:19px;margin-top:16px}
.discipline p{font-size:9.5px;line-height:16.5px;margin-top:10px;color:#e4ebf2}
.fiscal .center{text-align:center;margin-top:26px}

/* news */
.news{height:390px;background:linear-gradient(180deg,#e6e6e6,#f7f7f7)}
.news .section-title{padding-top:24px}
.news-list{display:flex;gap:20px;margin-top:12px}
.news-card{width:360px;height:287px;background:var(--white);box-shadow:0 1px 4px rgba(0,0,0,.1);padding:18px}
.news-img{height:138px}
.tag{display:flex;align-items:center;gap:6px;margin-top:18px}
.tag .ico{width:16px;height:16px;background:#444;display:flex;align-items:center;justify-content:center}
.tag .date{background:var(--sky);color:var(--white);font-size:7.5px;padding:3px 8px}
.news-card h3{font-size:14px;font-weight:500;margin-top:12px}
.news-card p{font-size:9.5px;line-height:15px;color:var(--muted);margin-top:6px}

/* product banner */
.product{height:393px;position:relative;background:linear-gradient(100deg,#c2602a 0%,#6a4a45 35%,#1f4d84 65%,#163a66 100%);overflow:hidden}
.product-photo{position:absolute;right:0;top:0;width:530px;height:393px;background:linear-gradient(180deg,rgba(233,232,230,.25),rgba(40,60,90,.2))}
.product-text{position:absolute;left:230px;top:60px;color:var(--white);width:420px}
.product-name{font-size:30px;font-weight:600;color:var(--white)}
.product-text h2{font-size:22px;line-height:31px;font-weight:600;margin-top:22px}
.product-text p{font-size:13px;line-height:22px;font-weight:300;margin-top:16px;color:#e8ecf1}
.product-text .btn{margin-top:22px;text-transform:none}

/* community */
.community{height:111px;background:var(--white)}
.community .wrap{display:flex;justify-content:center;align-items:center;gap:34px;height:111px}
.community h2{font-size:20px;font-weight:500;color:var(--ink);line-height:24px}
.community p{font-size:9.5px;color:var(--muted)}
.btn-sky{background:var(--sky);width:100px;text-align:center;padding:10px 0}

/* footer */
.footer{height:126px;background:var(--footer);color:#ddd}
.footer .wrap{display:flex;padding-top:25px}
.fcol{font-size:7px;line-height:12px;text-transform:uppercase;color:#c9c9c9}
.fcol h4{font-size:9.5px;font-weight:600;color:var(--white);text-transform:none;margin-bottom:8px}
.bottom{height:25px;background:var(--footer-dark);color:#bbb;font-size:7px;text-align:center;line-height:25px}
</style>
</head>
<body>

<div class="topbar">
  <div class="wrap">
    <span>Helpdesk: +31 (0)20 555 0141 &nbsp;|&nbsp; Fax: +31 (0)20 555 0199</span>
    <div class="flags">
      <div class="flag"><span style="background:#ae1c28"></span><span style="background:#fff"></span><span style="background:#21468b"></span></div>
      <div class="flag" style="flex-direction:row"><span style="background:#169b62"></span><span style="background:#fff"></span><span style="background:#ff883e"></span></div>
      <div class="flag"><span style="background:#c8102e"></span><span style="background:#fff"></span><span style="background:#012169"></span></div>
    </div>
  </div>
</div>

<header class="nav">
  <div class="wrap">
    <div class="brand"><i></i>QRS Software</div>
    <nav class="menu">
      <span>Who We Are</span><span>Learn QRS</span><span>Awards</span><span>Events</span><span>Novara</span>
      <span class="btn">Join Us</span>
    </nav>
  </div>
</header>

<section class="hero">
  <div class="hero-photo" role="img" aria-label="Photo of a smiling businessman holding a folder in an office"></div>
  <div class="hero-text">
    <h1>Technology Business<br>Management</h1>
    <p>Effective and affordable</p>
    <span class="btn">Know More</span>
  </div>
</section>

<section class="enable">
  <div class="wrap">
    <h2 class="section-title">Enable The Right Business Conversations</h2>
    <div class="cards">
      <div class="card">
        <svg viewBox="0 0 60 60"><circle cx="30" cy="30" r="26" fill="none" stroke="var(--orange)" stroke-width="5"/><circle cx="30" cy="30" r="4" fill="var(--orange)"/><path d="M30 30 L44 18" stroke="var(--orange)" stroke-width="4" stroke-linecap="round"/><path d="M14 34h5M41 34h5M30 12v5M18 20l3 3" stroke="var(--orange)" stroke-width="3"/></svg>
        <h3>Cost Of<br>Performance</h3>
        <p>Deliver technology, services, and projects efficiently to the business.</p>
      </div>
      <div class="card">
        <svg viewBox="0 0 60 60"><rect x="14" y="6" width="32" height="50" fill="var(--orange)"/><g fill="#fff"><rect x="19" y="12" width="6" height="5"/><rect x="27" y="12" width="6" height="5"/><rect x="35" y="12" width="6" height="5"/><rect x="19" y="21" width="6" height="5"/><rect x="27" y="21" width="6" height="5"/><rect x="35" y="21" width="6" height="5"/><rect x="19" y="30" width="6" height="5"/><rect x="27" y="30" width="6" height="5"/><rect x="35" y="30" width="6" height="5"/><rect x="26" y="44" width="8" height="12"/></g></svg>
        <h3>Business-Aligned<br>Portfolio</h3>
        <p>Optimize portfolios to deliver the most value for the level of spending.</p>
      </div>
      <div class="card">
        <svg viewBox="0 0 60 60"><path d="M30 12a15 15 0 0 0-9 27v6h18v-6a15 15 0 0 0-9-27z" fill="var(--orange)"/><rect x="22" y="48" width="16" height="4" fill="var(--orange)"/><path d="M32 18l-7 12h6l-3 10 8-13h-6z" fill="#fff"/><path d="M30 2v5M10 12l4 3M50 12l-4 3M4 30h5M51 30h5" stroke="var(--orange)" stroke-width="3"/></svg>
        <h3>Investment In<br>Innovation</h3>
        <p>Allocate adequate resources on new and enhanced services and on business innovation.</p>
      </div>
      <div class="card">
        <svg viewBox="0 0 60 60"><circle cx="30" cy="30" r="26" fill="var(--orange)"/><path d="M30 18l9 7-3 10h-12l-3-10z" fill="#fff"/><path d="M30 18V6M39 25l12-4M36 35l7 10M24 35l-7 10M21 25L9 21" stroke="#fff" stroke-width="2.5"/></svg>
        <h3>Enterprise<br>Agility</h3>
        <p>Help the business respond quickly to market opportunities or threats.</p>
      </div>
    </div>
  </div>
</section>

<section class="foster">
  <div class="wrap">
    <h2 class="section-title">Foster a Business Culture in IT</h2>
    <div class="pillars">
      <div class="pillar">
        <svg viewBox="0 0 80 76" role="img" aria-label="Illustration of a business team"><rect x="0" y="0" width="80" height="76" rx="6" fill="var(--orange)" opacity=".85"/></svg>
        <h3>Position for Value</h3>
        <p>Define what you deliver in terms of business capabilities that are understood and valued by your business unit partners, so you can work together to improve business outcomes.</p>
        <span class="btn btn-ghost">Read More</span>
      </div>
      <div class="pillar">
        <svg viewBox="0 0 80 76"><g fill="var(--navy)"><rect x="4" y="48" width="11" height="28"/><rect x="20" y="38" width="11" height="38"/><rect x="36" y="42" width="11" height="34"/><rect x="52" y="30" width="11" height="46"/><rect x="68" y="20" width="11" height="56"/></g><path d="M6 36 L24 24 L40 30 L58 16 L74 6" fill="none" stroke="var(--orange)" stroke-width="3"/><g fill="var(--orange)"><circle cx="6" cy="36" r="4"/><circle cx="24" cy="24" r="4"/><circle cx="40" cy="30" r="4"/><circle cx="58" cy="16" r="4"/><circle cx="74" cy="6" r="4"/></g></svg>
        <h3>Continuously Improve</h3>
        <p>Execute a strategic roadmap for QRS maturity by integrating QRS into your day-to-day processes and thinking, so that QRS drives every value conversation with your peers</p>
        <span class="btn btn-ghost">Read More</span>
      </div>
    </div>
  </div>
</section>

<section class="fiscal">
  <div class="wrap">
    <h2 class="section-title">Develop Sound Fiscal Disciplines</h2>
    <div class="disciplines">
      <div class="discipline">
        <svg viewBox="0 0 66 66"><rect x="2" y="2" width="62" height="62" fill="none" stroke="#fff" stroke-width="3"/><rect x="12" y="12" width="42" height="42" fill="#fff"/><path d="M17 33c8-12 24-12 32 0c-8 12-24 12-32 0z" fill="var(--orange)"/><circle cx="33" cy="33" r="5" fill="var(--navy)"/></svg>
        <h3>Create<br>Transparency</h3>
        <p>Translate your spending, consumption, and capacity into meaningful perspectives for technology and business decision-makers.</p>
      </div>
      <div class="discipline">
        <svg viewBox="0 0 66 66"><rect x="2" y="2" width="62" height="62" fill="none" stroke="#fff" stroke-width="3"/><rect x="12" y="12" width="42" height="42" fill="#fff"/><g fill="var(--orange)"><rect x="18" y="36" width="6" height="12"/><rect x="27" y="32" width="6" height="16"/><rect x="36" y="28" width="6" height="20"/><rect x="45" y="22" width="5" height="26"/></g><path d="M18 30l10-8 8 4 12-10" fill="none" stroke="var(--orange)" stroke-width="2.5"/></svg>
        <h3>Shape<br>Business Demand</h3>
        <p>Communicate costs and consumption to business units to drive informed trade-off decisions and better consumption behavior.</p>
      </div>
      <div class="discipline">
        <svg viewBox="0 0 66 66"><rect x="2" y="2" width="62" height="62" fill="none" stroke="#fff" stroke-width="3"/><rect x="12" y="12" width="42" height="42" fill="#fff"/><text x="33" y="45" text-anchor="middle" font-family="Poppins,sans-serif" font-weight="700" font-size="30" fill="var(--orange)">$</text></svg>
        <h3>Deliver Value<br>For Money</h3>
        <p>Maximize value and demonstrate industry-comparable cost-effectiveness for services and innovation you provide.</p>
      </div>
      <div class="discipline">
        <svg viewBox="0 0 66 66"><rect x="2" y="2" width="62" height="62" fill="none" stroke="#fff" stroke-width="3"/><rect x="12" y="12" width="42" height="42" fill="#fff"/><path d="M20 46 C24 34 34 38 40 26" fill="none" stroke="var(--orange)" stroke-width="2.5" stroke-dasharray="3 3"/><path d="M36 22l6 2-2 6" fill="none" stroke="var(--orange)" stroke-width="2.5"/><path d="M17 18l6 6M23 18l-6 6M40 40l6 6M46 40l-6 6" stroke="var(--navy)" stroke-width="2.5"/><circle cx="20" cy="46" r="3" fill="var(--orange)"/></svg>
        <h3>Plan &amp;<br>Govern</h3>
        <p>Collaborate to align your annual budget and resource plans to strategic business priorities and manage to the plan.</p>
      </div>
    </div>
    <div class="center"><span class="btn" style="text-transform:none">Know More</span></div>
  </div>
</section>

<section class="news">
  <div class="wrap">
    <h2 class="section-title">News</h2>
    <div class="news-list">
      <article class="news-card">
        <div class="news-img" role="img" aria-label="Photo of a business meeting beside a board of sticky notes" style="background:linear-gradient(90deg,#cfc6b8,#3a3f48 50%,#8e8880)"></div>
        <div class="tag"><span class="ico"><svg width="10" height="10" viewBox="0 0 10 10"><path d="M1 4h2l4-3v8L3 6H1z" fill="#fff"/></svg></span><span class="date">27 Feb 18</span></div>
        <h3>PriceLumen QRS Cost model</h3>
        <p>Define what you deliver in terms of business capabilities that are understood and valued by your business unit partners, so you can work together to improve business outcomes[...]</p>
      </article>
      <article class="news-card">
        <div class="news-img" role="img" aria-label="Photo of a group of colleagues in a training session" style="background:linear-gradient(180deg,#e3e2dd,#7d7b78 55%,#4d5560)"></div>
        <div class="tag"><span class="ico"><svg width="10" height="10" viewBox="0 0 10 10"><path d="M1 4h2l4-3v8L3 6H1z" fill="#fff"/></svg></span><span class="date">27 Feb 18</span></div>
        <h3>Cost Management Training Course Vietnam</h3>
        <p>Define what you deliver in terms of business capabilities that are understood and valued by your business unit partners, so you can work together to improve business outcomes[...]</p>
      </article>
    </div>
  </div>
</section>

<section class="product">
  <div class="product-photo" role="img" aria-label="Photo of a businesswoman pointing with a pen while holding a tablet"></div>
  <div class="product-text">
    <div class="product-name">PriceLumen</div>
    <h2>PriceLumen To Manage Your Costs,<br>Capacity, Revenues And Margins</h2>
    <p>Since 1992, Ledgerline has played a significant role in helping companies better understand their cost flow.</p>
    <span class="btn">Know More</span>
  </div>
</section>

<section class="community">
  <div class="wrap">
    <div>
      <h2>Join the most happening community</h2>
      <p>Lorem Ipsum is simply dummy text of the printing and typesetting industry.</p>
    </div>
    <span class="btn btn-sky">Join Now</span>
  </div>
</section>

<footer class="footer">
  <div class="wrap">
    <div class="fcol" style="width:101px"><h4>Product</h4>Overview<br>Details<br>Functions<br>Screenshots</div>
    <div class="fcol" style="width:103px"><h4>Markets</h4>Healthcare<br>City Councils<br>Banks<br>Telecom</div>
    <div class="fcol" style="width:121px"><h4>Partner</h4>Dedicated Partners<br>Independent Consulting<br>Affiliates</div>
    <div class="fcol" style="width:117px"><h4>Support</h4>Downloads<br>Licenses<br>Known Issues</div>
    <div class="fcol" style="width:155px"><h4>Contact Netherlands</h4>Tel: +31 (0)20 555 0123<br>Helpdesk: +31 (0)20 555 0141<br>Fax: +31 (0)20 555 0199</div>
    <div class="fcol"><h4>Contact USA</h4>Tel: +1 410 555 0172<br>Helpdesk: +31 (0)20 555 0141<br>Fax: +31 (0)20 555 0199</div>
  </div>
</footer>
<div class="bottom">© Ledgerline BV 2018 | Privacy Policy | Terms of Use</div>

</body>
</html>
```